Lotus Leaf Kitchen Road Billboard

Road Billboard I need all of this information on it
Authentic Thai Food Bangkok Style
6.5 Miles on the right
4126 Maple Ridge Rd Otto NC
828-555-4172

```html
<!DOCTYPE html>
<html lang="en">
<head>
<meta charset="utf-8">
<title>Lotus Leaf Kitchen Road Billboard</title>
<link rel="stylesheet" href="https://fonts.googleapis.com/css2?family=Playfair+Display:wght@500;600&family=Noto+Sans:wght@500;700&display=swap">
<style>
  :root {
    --page-bg: #bdd3ec;
    --gold: #dcae17;
    --white: #ffffff;
    --ink: #111111;
    --night-top: #27303d;
    --night-mid: #343c48;
    --night-glow: #6a5536;
    --wok-core: #3a2618;
    --wok-flame: #c8651c;
  }
  * { margin: 0; padding: 0; box-sizing: border-box; }
  html, body {
    width: 767px; height: 1200px; overflow: hidden;
    background: var(--page-bg);
  }
  .billboard {
    position: absolute; left: 64px; top: 440px;
    width: 639px; height: 319px;
    overflow: hidden;
    background: var(--white);
  }
  .hero {
    position: absolute; left: 0; top: 0; width: 639px; height: 270px;
    background: linear-gradient(180deg, var(--night-top) 0%, var(--night-mid) 45%, var(--night-glow) 85%, #3b3a3c 100%);
  }
  .accent-leaf { position: absolute; left: 0; top: 0; }
  .dish-photo {
    position: absolute; left: 329px; top: 46px; width: 310px; height: 200px;
    border-radius: 40% 30% 50% 50% / 40% 30% 60% 60%;
    background: radial-gradient(ellipse at 45% 55%, var(--wok-flame) 0%, var(--wok-core) 60%, rgba(30,25,22,0.9) 100%);
  }
  .brand {
    position: absolute; left: 40px; top: 30px; width: 202px;
    text-align: center;
  }
  .brand-dot {
    display: block; width: 24px; height: 24px; margin: 0 auto 12px;
    border-radius: 50%; background: var(--gold);
  }
  .brand-name {
    font-family: "Playfair Display", serif; font-weight: 500;
    font-size: 13px; color: var(--gold); letter-spacing: 0.3px;
  }
  .headline {
    position: absolute; left: 20px; top: 118px; width: 262px;
    text-align: center;
    font-family: "Playfair Display", serif; font-weight: 600;
    color: var(--white); font-size: 42px; line-height: 42px;
    letter-spacing: -0.5px;
  }
  .tagline {
    position: absolute; left: 20px; top: 211px; width: 262px;
    text-align: center;
    font-family: "Playfair Display", serif; font-weight: 500;
    color: var(--gold); font-size: 29px; line-height: 32px;
    letter-spacing: -0.5px;
  }
  .info-band {
    position: absolute; left: 0; top: 270px; width: 639px; height: 49px;
    background: var(--white);
    display: flex; align-items: center;
    font-family: "Noto Sans", sans-serif; color: var(--ink);
  }
  .info-icon { position: absolute; top: 11px; }
  .phone-icon { left: 34px; }
  .pin-icon { left: 230px; }
  .phone-number {
    position: absolute; left: 76px; top: 10px;
    font-size: 20px; font-weight: 700; line-height: 28px;
  }
  .directions {
    position: absolute; left: 264px; top: 13px;
    font-size: 14px; font-weight: 500; line-height: 24px;
  }
</style>
</head>
<body>
  <section class="billboard">
    <div class="hero" role="img" aria-label="Night skyline of Bangkok with city lights along the river"></div>
    <svg class="accent-leaf" width="639" height="270" viewBox="0 0 639 270" aria-hidden="true">
      <path d="M639 29 L639 62 C612 160 560 246 462 262 L376 266 L376 238 C398 150 470 40 639 29 Z" fill="var(--gold)"/>
    </svg>
    <div class="dish-photo" role="img" aria-label="Flaming wok tossing shrimp, broccoli and vegetables"></div>

    <div class="brand">
      <span class="brand-dot"></span>
      <p class="brand-name">Lotus Leaf Kitchen</p>
    </div>
    <h1 class="headline">AUTHENTIC<br>THAI FOOD</h1>
    <p class="tagline">BANGKOK STYLE</p>

    <div class="info-band">
      <svg class="info-icon phone-icon" width="26" height="26" viewBox="0 0 26 26" aria-hidden="true">
        <circle cx="13" cy="13" r="13" fill="var(--ink)"/>
        <path d="M8.5 7.5 L10.5 7 L12 10 L10.8 11.2 C11.5 12.8 12.8 14.2 14.5 15 L15.8 13.8 L18.8 15.3 L18.3 17.4 C17.8 18.4 16.5 18.8 15 18.2 C11.5 16.8 9 14.2 7.7 10.8 C7.2 9.3 7.6 8 8.5 7.5 Z" fill="var(--gold)"/>
        <path d="M14.5 7.5 A4 4 0 0 1 18.5 11.5 M14.5 5.5 A6 6 0 0 1 20.5 11.5" stroke="var(--gold)" stroke-width="1.2" fill="none" stroke-linecap="round"/>
      </svg>
      <span class="phone-number">828-555-4172</span>

      <svg class="info-icon pin-icon" width="26" height="26" viewBox="0 0 26 26" aria-hidden="true">
        <circle cx="13" cy="13" r="13" fill="var(--ink)"/>
        <path d="M13 6.5 C10.2 6.5 8.3 8.5 8.3 11 C8.3 14.2 13 19.5 13 19.5 C13 19.5 17.7 14.2 17.7 11 C17.7 8.5 15.8 6.5 13 6.5 Z" fill="var(--gold)"/>
        <circle cx="13" cy="11" r="1.7" fill="var(--ink)"/>
      </svg>
      <span class="directions">6.5 Miles on the right 4126 Maple Ridge Rd Otto NC</span>
    </div>
  </section>
</body>
</html>
```